Business Card Design

I would like to have business cards completely redesigned for my car ceramic coating and detailing business.
The cards uploaded are the current, the information needs to change but you can see our logo, I want something modern, professional and eye catching.

```html
<!DOCTYPE html>
<html lang="en">
<head>
<meta charset="utf-8">
<title>Sterling Shine – Business Card</title>
<link href="https://fonts.googleapis.com/css2?family=Montserrat:wght@500;700;800&family=Open+Sans:wght@400;600&display=swap" rel="stylesheet">
<style>
  :root {
    --brand-blue: #1f7fd6;
    --brand-blue-deep: #1763b0;
    --pattern-blue: #2a86dc;
    --ink: #3d3d3d;
    --ink-soft: #5a5a5a;
    --paper: #ffffff;
    --backdrop: #e9eaec;
    --rule: #d6d6d6;
  }
  * { box-sizing: border-box; margin: 0; padding: 0; }
  html, body { width: 1200px; height: 716px; overflow: hidden; }
  body {
    background: var(--backdrop);
    font-family: "Open Sans", sans-serif;
    position: relative;
  }
  .card {
    position: absolute;
    top: 203px;
    width: 540px;
    height: 310px;
    background: var(--paper);
    box-shadow: 0 6px 18px rgba(0,0,0,0.18);
    overflow: hidden;
  }
  .card--back { left: 45px; }
  .card--front { left: 615px; }

  /* Back side */
  .back-pattern {
    position: absolute; inset: 0;
    background: radial-gradient(circle at 50% 50%, var(--pattern-blue), var(--brand-blue-deep));
  }
  .back-wordmark {
    position: absolute;
    left: 50%; top: 50%;
    transform: translate(-50%, -50%);
    font-family: "Montserrat", sans-serif;
    font-weight: 800;
    font-size: 38px;
    letter-spacing: 1px;
    color: var(--paper);
    display: flex; align-items: center; gap: 12px;
  }
  .back-wordmark .mark-dot {
    width: 14px; height: 14px; border-radius: 50%; background: var(--paper);
  }

  /* Front side */
  .front-brand {
    position: absolute;
    left: 30px; top: 62px;
    width: 200px; height: 110px;
    display: flex; align-items: center; justify-content: center; gap: 10px;
    font-family: "Montserrat", sans-serif;
    font-weight: 800;
    font-size: 26px;
    line-height: 1.05;
    color: var(--ink);
    text-align: center;
  }
  .front-brand .mark-square {
    width: 14px; height: 14px; background: var(--ink); flex: none;
  }
  .divider {
    position: absolute;
    left: 246px; top: 60px;
    width: 1px; height: 116px;
    background: var(--rule);
  }
  .contact {
    position: absolute;
    left: 264px; top: 58px;
  }
  .contact__name {
    font-family: "Montserrat", sans-serif;
    font-weight: 700;
    font-size: 19px;
    color: var(--brand-blue);
    text-transform: uppercase;
    letter-spacing: 0.3px;
  }
  .contact__role {
    font-size: 12.5px;
    color: var(--ink-soft);
    line-height: 1.35;
    margin-top: 2px;
  }
  .contact__list { list-style: none; margin-top: 6px; }
  .contact__list li {
    display: flex; align-items: center; gap: 7px;
    font-size: 12.5px; color: var(--ink); line-height: 1.6;
  }
  .contact__list svg { width: 11px; height: 11px; fill: var(--ink); flex: none; }

  .address-band {
    position: absolute;
    left: 0; right: 0; top: 208px;
    height: 34px;
    background: var(--brand-blue);
    color: var(--paper);
    font-family: "Montserrat", sans-serif;
    font-weight: 500;
    font-size: 13px;
    display: flex; align-items: center;
    padding-left: 52px;
  }
  .base-stripe {
    position: absolute;
    left: 0; right: 0; bottom: 0;
    height: 22px;
    background: var(--brand-blue);
  }
</style>
</head>
<body>

  <section class="card card--back">
    <div class="back-pattern" role="img" aria-label="Repeating pattern of gem shapes on blue"></div>
    <div class="back-wordmark"><span class="mark-dot"></span>Sterling Shine</div>
  </section>

  <section class="card card--front">
    <div class="front-brand"><span class="mark-square"></span>Sterling<br>Shine</div>
    <div class="divider"></div>

    <div class="contact">
      <h1 class="contact__name">Renée Callister</h1>
      <p class="contact__role">Owner I Operator<br>Automotive Detailing</p>
      <ul class="contact__list">
        <li>
          <svg viewBox="0 0 24 24"><path d="M6.6 10.8a15.1 15.1 0 0 0 6.6 6.6l2.2-2.2a1 1 0 0 1 1-.25 11.4 11.4 0 0 0 3.6.57 1 1 0 0 1 1 1V20a1 1 0 0 1-1 1A17 17 0 0 1 3 4a1 1 0 0 1 1-1h3.5a1 1 0 0 1 1 1c0 1.25.2 2.45.57 3.57a1 1 0 0 1-.25 1z"/></svg>
          0400 123 456
        </li>
        <li>
          <svg viewBox="0 0 24 24"><path d="M2 5h20v14H2z M2 5l10 8 10-8" fill="none" stroke="#3d3d3d" stroke-width="2.4"/></svg>
          bookings@sterlingshine.com.au
        </li>
        <li>
          <svg viewBox="0 0 24 24"><circle cx="12" cy="12" r="10"/><path d="M2 12h20M12 2c3 3 3 17 0 20M12 2c-3 3-3 17 0 20" stroke="#fff" stroke-width="1.5" fill="none"/></svg>
          www.sterlingshine.com.au
        </li>
      </ul>
    </div>

    <div class="address-band">Unit 4/22 Harlow Court Kingsford ACT 2610</div>
    <div class="base-stripe"></div>
  </section>

</body>
</html>
```